Financial Services Postcard Design

Lionel Budwig, CPA
Financial Services
Accounting/Tax/Consulting
Services include but not limited to
Financial Statements
Tax Returns
CFO/Controller services
Budgeting and Forecasting
Cash Management
Payroll / AP/ AR
Insurance Analysis
Cost Analysis
Special projects

I need a postcard design for my new financial service company to assist businesses in the Orange County area of southern California. I'm looking for a warm but bright look to represent CPA with many years of Management experience with manufacturing companies that can relate to business issues and provide solutions for small business.

```html
<!DOCTYPE html>
<html lang="en">
<head>
<meta charset="utf-8">
<title>Financial Services Postcard – Lionel Budwig, CPA</title>
<link rel="stylesheet" href="https://fonts.googleapis.com/css2?family=Source+Sans+3:wght@400;600;700&display=swap">
<style>
  :root {
    --navy: #1f2d5c;
    --blue: #1a8fd0;
    --sky: #2aa8e0;
    --deep: #0b5f8c;
    --name-blue: #2a6fb8;
    --ink: #1e2233;
    --muted: #8a8f98;
    --panel: #f1f1f1;
    --paper: #ffffff;
    --paper-tint: #f4f8fc;
    --stage: #e8ebef;
  }
  * { box-sizing: border-box; margin: 0; padding: 0; }
  html, body { width: 1200px; height: 667px; overflow: hidden; }
  body {
    background: var(--stage);
    font-family: "Source Sans 3", "Segoe UI", sans-serif;
    color: var(--ink);
    position: relative;
  }

  /* ---------- Flyer (front) ---------- */
  .flyer {
    position: absolute; left: 32px; top: 23px;
    width: 442px; height: 615px;
    background: var(--paper-tint);
    overflow: hidden;
  }
  .flyer__photo {
    position: absolute; left: 0; top: 0; width: 442px; height: 300px;
    background: linear-gradient(160deg, #3b4150 0%, #8e97a6 30%, #dfe6ee 60%, #9ec3e2 85%, #4f86c0 100%);
  }
  .flyer__shapes { position: absolute; left: 0; top: 0; }
  .flyer__heading {
    position: absolute; right: 22px; top: 287px; text-align: right;
  }
  .flyer__title { font-size: 22px; font-weight: 700; color: var(--navy); line-height: 1.1; }
  .flyer__tagline { font-size: 16.5px; color: var(--navy); line-height: 1.3; }
  .services__label {
    position: absolute; left: 24px; top: 369px;
    font-size: 16px; font-weight: 700; color: var(--navy);
  }
  .services__list {
    position: absolute; list-style: none;
    font-size: 16px; line-height: 20.3px; color: var(--ink);
  }
  .services__list--left { left: 30px; top: 398px; }
  .services__list--right { left: 272px; top: 398px; }
  .services__list li { display: flex; align-items: center; gap: 7px; }
  .bullet { width: 12px; height: 12px; flex: none; }
  .flyer__contact {
    position: absolute; right: 36px; top: 530px; text-align: right;
  }
  .flyer__name { font-size: 14px; color: var(--name-blue); }
  .flyer__phone {
    font-size: 16px; font-weight: 700; color: var(--navy);
    display: flex; align-items: center; justify-content: flex-end; gap: 8px; margin-top: 4px;
  }
  .flyer__band, .mailer__band {
    position: absolute; left: 0; bottom: 0; width: 100%;
    background: linear-gradient(90deg, var(--sky) 0%, #2a6aa3 55%, var(--navy) 100%);
  }
  .flyer__band { height: 22px; }

  /* ---------- Mailer (back) ---------- */
  .mailer {
    position: absolute; left: 546px; top: 197px;
    width: 614px; height: 443px;
    background: var(--paper);
    overflow: hidden;
  }
  .mailer__sender {
    position: absolute; left: 0; top: 101px; width: 344px; height: 221px;
    background: var(--panel);
    border: 1px solid #d3d3d3; border-left: none;
    border-bottom-right-radius: 9px;
  }
  .mailer__header { position: absolute; left: 0; top: 0; }
  .mailer__title {
    position: absolute; left: 0; top: 20px; width: 624px; text-align: center;
    font-size: 30px; font-weight: 700; color: #fff;
  }
  .mailer__tagline {
    position: absolute; left: 0; top: 58px; width: 624px; text-align: center;
    font-size: 21px; letter-spacing: 1px; color: #fff;
  }
  .sender__photo {
    position: absolute; left: 28px; top: 56px; width: 105px; height: 131px;
    background: linear-gradient(180deg, #e9e0c2 0%, #d8cfb2 45%, #2b3140 70%, #1c2029 100%);
  }
  .sender__name {
    position: absolute; left: 151px; top: 107px;
    font-size: 17.5px; color: var(--name-blue);
  }
  .sender__line {
    position: absolute; left: 148px;
    font-size: 13px; color: var(--muted);
    display: flex; align-items: center; gap: 8px;
  }
  .sender__line--phone { top: 144px; }
  .sender__line--email { top: 169px; }
  .stamp-box {
    position: absolute; left: 521px; top: 125px; width: 49px; height: 38px;
    border: 1px solid #9a9a9a;
  }
  .address-line {
    position: absolute; left: 423px; width: 144px; height: 0;
    border-top: 1px solid #a7a7a7;
  }
  .mailer__band { height: 23px; }
</style>
</head>
<body>

<!-- Flyer -->
<section class="flyer">
  <div class="flyer__photo" role="img" aria-label="Photo of business people reviewing financial bar charts at a desk"></div>

  <svg class="flyer__shapes" width="442" height="615" viewBox="0 0 442 615" aria-hidden="true">
    <defs>
      <linearGradient id="flyerSwoosh" x1="0" x2="1" y1="0" y2="0">
        <stop offset="0" stop-color="#2aa8e0"/>
        <stop offset="0.6" stop-color="#2a5fa0"/>
        <stop offset="1" stop-color="#1f2d5c"/>
      </linearGradient>
      <linearGradient id="flyerArc" x1="0" x2="1" y1="0" y2="0">
        <stop offset="0" stop-color="#2aa8e0" stop-opacity="0.4"/>
        <stop offset="0.5" stop-color="#2a6aa3"/>
        <stop offset="1" stop-color="#1f2d5c"/>
      </linearGradient>
    </defs>
    <path d="M0,300 C150,305 330,270 442,236 L442,615 L0,615 Z" fill="#f4f8fc"/>
    <path d="M0,262 C120,300 300,272 442,212 L442,236 C330,272 150,305 0,300 Z" fill="url(#flyerSwoosh)"/>
    <path d="M207,568 C280,522 360,500 442,489 L442,502 C360,510 280,532 207,568 Z" fill="url(#flyerArc)"/>
  </svg>

  <div class="flyer__heading">
    <h1 class="flyer__title">Financial Services</h1>
    <p class="flyer__tagline">Accounting &#9642; Tax &#9642; Consulting</p>
  </div>

  <h2 class="services__label">Our Services:</h2>
  <ul class="services__list services__list--left">
    <li><svg class="bullet" viewBox="0 0 12 12"><circle cx="6" cy="6" r="6" fill="#1a8fd0"/><path d="M4.8,3.5 L7.3,6 L4.8,8.5" stroke="#fff" stroke-width="1.6" fill="none"/></svg>Financial Statements</li>
    <li><svg class="bullet" viewBox="0 0 12 12"><circle cx="6" cy="6" r="6" fill="#1a8fd0"/><path d="M4.8,3.5 L7.3,6 L4.8,8.5" stroke="#fff" stroke-width="1.6" fill="none"/></svg>Tax Returns</li>
    <li><svg class="bullet" viewBox="0 0 12 12"><circle cx="6" cy="6" r="6" fill="#1a8fd0"/><path d="M4.8,3.5 L7.3,6 L4.8,8.5" stroke="#fff" stroke-width="1.6" fill="none"/></svg>CFO/Controller services</li>
    <li><svg class="bullet" viewBox="0 0 12 12"><circle cx="6" cy="6" r="6" fill="#1a8fd0"/><path d="M4.8,3.5 L7.3,6 L4.8,8.5" stroke="#fff" stroke-width="1.6" fill="none"/></svg>Budgeting and Forecasting</li>
    <li><svg class="bullet" viewBox="0 0 12 12"><circle cx="6" cy="6" r="6" fill="#1a8fd0"/><path d="M4.8,3.5 L7.3,6 L4.8,8.5" stroke="#fff" stroke-width="1.6" fill="none"/></svg>Cash Management</li>
  </ul>
  <ul class="services__list services__list--right">
    <li><svg class="bullet" viewBox="0 0 12 12"><circle cx="6" cy="6" r="6" fill="#1a8fd0"/><path d="M4.8,3.5 L7.3,6 L4.8,8.5" stroke="#fff" stroke-width="1.6" fill="none"/></svg>Payroll / AP/ AR</li>
    <li><svg class="bullet" viewBox="0 0 12 12"><circle cx="6" cy="6" r="6" fill="#1a8fd0"/><path d="M4.8,3.5 L7.3,6 L4.8,8.5" stroke="#fff" stroke-width="1.6" fill="none"/></svg>Insurance Analysis</li>
    <li><svg class="bullet" viewBox="0 0 12 12"><circle cx="6" cy="6" r="6" fill="#1a8fd0"/><path d="M4.8,3.5 L7.3,6 L4.8,8.5" stroke="#fff" stroke-width="1.6" fill="none"/></svg>Cost Analysis</li>
    <li><svg class="bullet" viewBox="0 0 12 12"><circle cx="6" cy="6" r="6" fill="#1a8fd0"/><path d="M4.8,3.5 L7.3,6 L4.8,8.5" stroke="#fff" stroke-width="1.6" fill="none"/></svg>Special projects</li>
  </ul>

  <div class="flyer__contact">
    <p class="flyer__name">Lionel Budwig, CPA</p>
    <p class="flyer__phone">
      <svg width="16" height="16" viewBox="0 0 24 24" aria-hidden="true"><path d="M6.6 10.8c1.4 2.8 3.8 5.1 6.6 6.6l2.2-2.2c.3-.3.7-.4 1-.2 1.1.4 2.3.6 3.6.6.6 0 1 .4 1 1V20c0 .6-.4 1-1 1C10.6 21 3 13.4 3 4c0-.6.4-1 1-1h3.5c.6 0 1 .4 1 1 0 1.3.2 2.5.6 3.6.1.3 0 .7-.2 1l-2.3 2.2z" fill="#1f2d5c"/></svg>
      714-555-0142
    </p>
  </div>

  <div class="flyer__band"></div>
</section>

<!-- Mailer -->
<section class="mailer">
  <div class="mailer__sender">
    <div class="sender__photo" role="img" aria-label="Portrait photo of Lionel Budwig in a dark suit"></div>
    <p class="sender__name">Lionel Budwig, CPA</p>
    <p class="sender__line sender__line--phone">
      <svg width="10" height="10" viewBox="0 0 24 24" aria-hidden="true"><path d="M6.6 10.8c1.4 2.8 3.8 5.1 6.6 6.6l2.2-2.2c.3-.3.7-.4 1-.2 1.1.4 2.3.6 3.6.6.6 0 1 .4 1 1V20c0 .6-.4 1-1 1C10.6 21 3 13.4 3 4c0-.6.4-1 1-1h3.5c.6 0 1 .4 1 1 0 1.3.2 2.5.6 3.6.1.3 0 .7-.2 1l-2.3 2.2z" fill="#9a9ea6"/></svg>
      714-555-0142
    </p>
    <p class="sender__line sender__line--email">
      <svg width="11" height="8" viewBox="0 0 11 8" aria-hidden="true"><rect width="11" height="8" rx="1" fill="#b3b6bc"/><path d="M0.5,0.8 L5.5,4.5 L10.5,0.8" stroke="#f1f1f1" stroke-width="1" fill="none"/></svg>
      LionelBudwig@ocledger.net
    </p>
  </div>

  <svg class="mailer__header" width="614" height="130" viewBox="0 0 614 130" aria-hidden="true">
    <defs>
      <linearGradient id="headerFill" x1="0" x2="0" y1="0" y2="1">
        <stop offset="0" stop-color="#2aa8e0"/>
        <stop offset="1" stop-color="#0b5f8c"/>
      </linearGradient>
    </defs>
    <path d="M0,0 H614 V102 C500,118 380,122 270,116 C160,110 70,96 0,86 Z" fill="url(#headerFill)"/>
    <path d="M0,76 C80,92 180,110 300,118 C180,114 80,108 0,106 Z" fill="#7cc7ea"/>
  </svg>
  <h1 class="mailer__title">Financial Services</h1>
  <p class="mailer__tagline">Accounting &#9642; Tax &#9642; Consulting</p>

  <div class="stamp-box"></div>
  <div class="address-line" style="top:206px"></div>
  <div class="address-line" style="top:233px"></div>
  <div class="address-line" style="top:261px"></div>

  <div class="mailer__band"></div>
</section>

</body>
</html>
```